Rivolex.com Trucking Company Website

Need a website designed (no content) for a trucking company, specializing in trucking of ocean containers (intermodal Trucking). Heavy emphasis on technology, using latest technology, providing unabated visibility and realtime information.
clean minimalist industrial website
example:
https://www.bramtiq.com/

Target Market(s)

Professional Business Consumer corporate and small business

Industry/Entity Type

Trucking Company

Number of Pages Required

5+ page

Requirements
Must have
• Industrial Design, simple informative, for a busy professional to view and get the necessary information with out the distractions.
• Blog Page
• Client Log-In on the front page
• Technology page - showing our intensive investments in technology
Nice to have
• If ANY images included, MUST be USA related. Example if include an image of a truck, ensure its a USA model. Do the research.
• included our business card for sample of Logo
• Doesnt not have to be the same color schemes.
Should not have
• moving images

```html
<!DOCTYPE html>
<html lang="en">
<head>
<meta charset="utf-8">
<title>Rivolex.com — Intermodal Trucking</title>
<link rel="stylesheet" href="https://fonts.googleapis.com/css2?family=Open+Sans:ital,wght@0,400;0,600;0,700;1,400;1,600&display=swap">
<style>
:root{
  --blue:#0e88c9;
  --blue-dark:#0a6fa6;
  --orange:#f7941d;
  --ink:#333;
  --muted:#777;
  --white:#fff;
  --bar:rgba(20,30,45,.55);
}
*{box-sizing:border-box;margin:0;padding:0}
html,body{width:1200px;height:3377px;overflow:hidden}
body{position:relative;font-family:"Open Sans",Arial,sans-serif;color:var(--ink);background:var(--white)}
.abs{position:absolute}

/* hero */
.hero{left:0;top:0;width:1200px;height:552px;background:
  linear-gradient(90deg,rgba(0,0,0,.35) 0%,rgba(0,0,0,0) 55%),
  linear-gradient(100deg,#f2b04d 0%,#c9783a 18%,#5a3a33 32%,#7a1c1c 45%,#a8262a 65%,#4d1014 85%,#2a0d10 100%)}
.hero-shade{left:0;top:380px;width:1200px;height:172px;background:linear-gradient(180deg,rgba(0,0,0,0),rgba(0,0,0,.55))}
.topbar{left:0;top:0;width:1200px;height:45px;background:var(--bar)}
.login-field{top:10px;width:155px;height:25px;background:#e6e6e6;border:1px solid #ccc;font-size:12px;color:#888;padding:4px 10px}
.login-btn{left:420px;top:10px;width:77px;height:25px;border-radius:13px;background:var(--orange);color:var(--white);font-size:12px;font-weight:700;text-align:center;line-height:25px}
.contact-mini{top:8px;color:var(--white);font-size:12px;line-height:14px}
.contact-mini b{font-weight:700;font-size:11px;display:block}
.hire{left:961px;top:0;width:239px;height:45px;background:var(--orange);color:var(--white);font-weight:700;font-size:15px;text-align:center;line-height:45px}
.logo{left:74px;top:64px;color:var(--white);font-weight:700;font-size:30px;letter-spacing:1px;display:flex;align-items:center;gap:10px}
.logo i{display:inline-block;width:18px;height:18px;background:var(--white)}
.nav{left:490px;top:80px;display:flex;gap:0;color:var(--white);font-size:14px}
.nav span{display:block;padding:0 24px;height:34px;line-height:20px}
.nav .active{border-bottom:3px solid var(--blue)}
.hero-title{left:72px;top:372px;color:var(--white);font-size:50px;font-weight:600}
.hero-sub{left:74px;top:440px;color:var(--white);font-size:16px;line-height:23px}

/* features */
.feature{top:612px;width:360px;text-align:center}
.feature .photo{width:153px;height:153px;border-radius:50%;margin:0 auto;border:6px solid #f1f1f1;box-shadow:0 2px 6px rgba(0,0,0,.2)}
.feature h3{color:var(--blue);font-size:14px;font-weight:700;margin-top:28px}
.feature p{color:var(--muted);font-size:12px;font-style:italic;line-height:19px;margin:6px auto 0;width:250px}
.feature .more{color:var(--orange);font-size:14px;margin-top:14px}

/* why */
.why-photo{left:0;top:930px;width:599px;height:554px;background:linear-gradient(180deg,#a9c6df 0%,#d8e4ec 40%,#c9a44a 55%,#b07a35 70%,#8f8b86 85%,#a9a7a2 100%)}
.why{left:599px;top:930px;width:601px;height:554px;background:var(--blue);color:var(--white)}
.why h2{position:absolute;left:106px;top:82px;font-size:28px;font-weight:700;color:var(--white)}
.why h2::after{content:"";position:absolute;left:0;top:50px;width:70px;height:4px;background:var(--orange)}
.why-item{position:absolute;left:106px;width:440px;font-size:15px;line-height:24px}
.why-item b{font-weight:700;display:block}
.why-icon{position:absolute;left:-62px;top:4px;width:46px;height:46px}

/* services */
.services-title{left:0;top:1560px;width:1200px;text-align:center;color:var(--blue);font-size:32px;font-weight:700}
.tile{width:241px;height:275px;background:var(--blue);color:var(--white);text-align:center}
.tile svg{position:absolute;left:62px;top:50px}
.tile h4{position:absolute;left:0;width:100%;top:190px;font-size:24px;font-weight:700}
.tile.featured{background:var(--orange);box-shadow:0 8px 18px rgba(0,0,0,.3)}
.tile.featured h4{top:54px;font-weight:400}
.tile.featured p{position:absolute;left:30px;width:181px;top:150px;font-size:15px;line-height:22px}

/* testimonial */
.testimonial{left:0;top:2364px;width:1200px;height:367px;background:linear-gradient(100deg,#f4f5f7 0%,#eceef1 45%,#e7e0d6 75%,#e9e3da 100%)}
.partner{left:74px;top:2505px;font-size:52px;font-weight:700;color:#1f4f93;display:flex;align-items:center;gap:16px}
.partner i{display:inline-block;width:34px;height:34px;background:#1f4f93}
.quote-name{left:522px;top:2482px;color:var(--blue);font-size:14px;font-style:italic;font-weight:600}
.quote{left:522px;top:2515px;width:600px;color:#666;font-size:22px;font-style:italic;line-height:30px}

/* contact */
.contact{left:0;top:2731px;width:1200px;height:552px;background:var(--blue);color:var(--white)}
.contact h2{position:absolute;left:74px;top:80px;font-size:32px;font-weight:700}
.contact h2::after{content:"";position:absolute;left:0;top:52px;width:66px;height:4px;background:var(--orange)}
.contact .lead{position:absolute;left:98px;top:162px;font-size:15px;font-weight:700}
.contact .group{position:absolute;left:98px;font-size:15px;line-height:32px}
.contact .group b{display:block;font-weight:700}
.contact .row{display:flex;align-items:center;gap:20px}
.pill{position:absolute;top:446px;height:32px;border:2px solid var(--white);border-radius:16px;font-size:12px;font-weight:700;line-height:28px;padding:0 12px}
.map{left:610px;top:2801px;width:590px;height:515px;background:linear-gradient(135deg,#eae6d8 0%,#f3efe0 40%,#e4e8d2 70%,#cfe0ea 100%);border:6px solid var(--white);box-shadow:0 2px 10px rgba(0,0,0,.25)}

/* footer */
.footer{left:0;top:3283px;width:1200px;height:94px;background:var(--orange);color:var(--white);padding:40px 0 0 74px;font-size:14px;font-weight:700}
</style>
</head>
<body>

<header>
  <div class="abs hero" role="img" aria-label="Photo of a red semi-truck trailer on a highway at sunset"></div>
  <div class="abs hero-shade"></div>
  <div class="abs topbar"></div>
  <div class="abs login-field" style="left:74px">Username</div>
  <div class="abs login-field" style="left:252px">Password</div>
  <div class="abs login-btn">LOGIN</div>
  <svg class="abs" style="left:612px;top:10px" width="22" height="22" viewBox="0 0 24 24"><path fill="#fff" d="M6.6 10.8a15 15 0 0 0 6.6 6.6l2.2-2.2c.3-.3.7-.4 1-.2 1.1.4 2.3.6 3.6.6.6 0 1 .4 1 1V20c0 .6-.4 1-1 1A17 17 0 0 1 3 4c0-.6.4-1 1-1h3.5c.6 0 1 .4 1 1 0 1.3.2 2.5.6 3.6.1.3 0 .7-.2 1z"/></svg>
  <div class="abs contact-mini" style="left:645px"><b>Phone</b>(+00) 000 000</div>
  <svg class="abs" style="left:793px;top:11px" width="26" height="20" viewBox="0 0 26 20"><rect x="1" y="1" width="24" height="18" fill="none" stroke="#fff" stroke-width="2"/><path d="M1 1l12 10L25 1" fill="none" stroke="#fff" stroke-width="2"/></svg>
  <div class="abs contact-mini" style="left:833px"><b>Email</b>info@rivolex.com</div>
  <div class="abs hire">HIRE A TRUCK</div>
  <div class="abs logo"><i></i>RIVOLEX</div>
  <nav class="abs nav">
    <span class="active">HOME</span><span>ABOUT US</span><span>SERVICES</span><span>CONTACT</span><span>BLOG</span><span>TECHNOLOGY</span>
  </nav>
  <h1 class="abs hero-title">Suspendisse Potenti</h1>
  <p class="abs hero-sub">Vestibulum eget pharetra magna, a consequat lectus.<br>Vestibulum volutpat interdum dolor eu interdum.</p>
</header>

<section class="features">
  <div class="abs feature" style="left:61px">
    <div class="photo" role="img" aria-label="Photo of a black truck cab" style="background:radial-gradient(circle,#555 0%,#1a1a1a 70%)"></div>
    <h3>Services</h3>
    <p>Donec sagittis sapien velit, a convallis nisi consequat vitae.</p>
    <div class="more">See more &gt;&gt;</div>
  </div>
  <div class="abs feature" style="left:421px">
    <div class="photo" role="img" aria-label="Photo of a red truck cab" style="background:radial-gradient(circle,#e23a3a 0%,#9b1c1c 55%,#3a3a3a 100%)"></div>
    <h3>Visit our Blog</h3>
    <p>Duis arcu arcu, fringilla et nisl vitae, sollicitudin dignissim lectus.</p>
    <div class="more">See more &gt;&gt;</div>
  </div>
  <div class="abs feature" style="left:781px">
    <div class="photo" role="img" aria-label="Word cloud about technology" style="background:radial-gradient(circle,#fafafa 0%,#e2e2e2 100%)"></div>
    <h3>Technology</h3>
    <p>Donec sagittis sapien velit, a convallis nisi consequat vitae.</p>
    <div class="more">See more &gt;&gt;</div>
  </div>
</section>

<section class="why-section">
  <div class="abs why-photo" role="img" aria-label="Photo of a forklift loading boxes into a yellow container trailer"></div>
  <div class="abs why">
    <h2>WHY CHOOSE US ?</h2>
    <div class="why-item" style="top:191px">
      <svg class="why-icon" viewBox="0 0 46 46"><circle cx="23" cy="23" r="21" fill="none" stroke="#fff" stroke-width="2"/><path d="M23 11l3.5 7.5 8 1-6 5.5 1.6 8L23 29l-7.1 4 1.6-8-6-5.5 8-1z" fill="none" stroke="#fff" stroke-width="2" stroke-linejoin="round"/></svg>
      <b>Donec elementum tortor nulla</b>
      Sit amet rutrum felis venenatis sit amet. Fusce dictum magna a tellus dignissim auctor. Duis fermentum velit faucibus massa auctor tincidunt.
    </div>
    <div class="why-item" style="top:299px">
      <svg class="why-icon" viewBox="0 0 46 46"><circle cx="23" cy="23" r="21" fill="none" stroke="#fff" stroke-width="2"/><path d="M14 21h5v12h-5zM19 22l4-8c2 0 3 1 2.5 3.5L25 21h7c1.5 0 2.3 1.2 2 2.5l-2 8c-.3 1-1 1.5-2 1.5H19" fill="none" stroke="#fff" stroke-width="2" stroke-linejoin="round"/></svg>
      <b>Pellentesque purus neque</b>
      Sed ac ante tellus. Morbi eu mauris pellentesque, iaculis massa quis, dapibus arcu.
    </div>
    <div class="why-item" style="top:385px">
      <svg class="why-icon" viewBox="0 0 46 46"><circle cx="23" cy="23" r="21" fill="none" stroke="#fff" stroke-width="2"/><path d="M23 33l-9-9a5 5 0 0 1 9-6 5 5 0 0 1 9 6z" fill="none" stroke="#fff" stroke-width="2" stroke-linejoin="round"/></svg>
      <b>Integer sed urna non nullat</b>
      Vestibulum eget pharetra magna, a consequat lectus. Vestibulum volutpat interdum dolor eu interdum. Maecenas non mattis erat, nec lacinia arcu.
    </div>
  </div>
</section>

<section class="services">
  <h2 class="abs services-title">OUR SERVICES</h2>
  <div class="abs tile" style="left:74px;top:1677px"><svg width="117" height="117" viewBox="0 0 117 117"><circle cx="56" cy="61" r="50" fill="none" stroke="#fff" stroke-width="7"/><path d="M33 60l20 20 50-66" fill="none" stroke="#fff" stroke-width="8" stroke-linecap="round" stroke-linejoin="round"/></svg><h4>LACINIA ARCU</h4></div>
  <div class="abs tile" style="left:344px;top:1677px"><svg width="117" height="117" viewBox="0 0 117 117"><circle cx="56" cy="61" r="50" fill="none" stroke="#fff" stroke-width="7"/><path d="M33 60l20 20 50-66" fill="none" stroke="#fff" stroke-width="8" stroke-linecap="round" stroke-linejoin="round"/></svg><h4>PHASELLUS</h4></div>
  <div class="abs tile" style="left:615px;top:1677px"><svg width="117" height="117" viewBox="0 0 117 117"><circle cx="56" cy="61" r="50" fill="none" stroke="#fff" stroke-width="7"/><path d="M33 60l20 20 50-66" fill="none" stroke="#fff" stroke-width="8" stroke-linecap="round" stroke-linejoin="round"/></svg><h4>FRINGILLA</h4></div>
  <div class="abs tile" style="left:885px;top:1677px"><svg width="117" height="117" viewBox="0 0 117 117"><circle cx="56" cy="61" r="50" fill="none" stroke="#fff" stroke-width="7"/><path d="M33 60l20 20 50-66" fill="none" stroke="#fff" stroke-width="8" stroke-linecap="round" stroke-linejoin="round"/></svg><h4>VENENATIS</h4></div>
  <div class="abs tile" style="left:74px;top:1983px"><svg width="117" height="117" viewBox="0 0 117 117"><circle cx="56" cy="61" r="50" fill="none" stroke="#fff" stroke-width="7"/><path d="M33 60l20 20 50-66" fill="none" stroke="#fff" stroke-width="8" stroke-linecap="round" stroke-linejoin="round"/></svg><h4>CURSUS EGET</h4></div>
  <div class="abs tile" style="left:344px;top:1983px"><svg width="117" height="117" viewBox="0 0 117 117"><circle cx="56" cy="61" r="50" fill="none" stroke="#fff" stroke-width="7"/><path d="M33 60l20 20 50-66" fill="none" stroke="#fff" stroke-width="8" stroke-linecap="round" stroke-linejoin="round"/></svg><h4>TINCIDUNT</h4></div>
  <div class="abs tile featured" style="left:615px;top:1983px"><h4>DUIS ARCU</h4><p>Integer libero mauris, mattis sed dolor id, pretium mattis lacus.</p></div>
  <div class="abs tile" style="left:885px;top:1983px"><svg width="117" height="117" viewBox="0 0 117 117"><circle cx="56" cy="61" r="50" fill="none" stroke="#fff" stroke-width="7"/><path d="M33 60l20 20 50-66" fill="none" stroke="#fff" stroke-width="8" stroke-linecap="round" stroke-linejoin="round"/></svg><h4>MASSA AUCTOR</h4></div>
</section>

<section class="testimonial-section">
  <div class="abs testimonial" role="img" aria-label="Faded photo of a white truck on a curving highway"></div>
  <div class="abs partner"><i></i>HARBORLINE</div>
  <div class="abs quote-name">Mr. Dalton - Maecenas Harborline</div>
  <blockquote class="abs quote">“Aliquam venenatis viverra lectus, quis ullamcorper mi pulvinar id. Nullam sed nibh justo. Nunc metus dolor, cursus eget sollicitudin feugiat, consectetur in nibh.”</blockquote>
</section>

<section class="abs contact">
  <h2>CONTACT</h2>
  <p class="lead">Please do not hesitate to contact us through:</p>
  <div class="group" style="top:210px">
    <b>Headquater</b>
    <div class="row"><svg width="14" height="14" viewBox="0 0 24 24"><path fill="#fff" d="M6.6 10.8a15 15 0 0 0 6.6 6.6l2.2-2.2c.3-.3.7-.4 1-.2 1.1.4 2.3.6 3.6.6.6 0 1 .4 1 1V20c0 .6-.4 1-1 1A17 17 0 0 1 3 4c0-.6.4-1 1-1h3.5c.6 0 1 .4 1 1 0 1.3.2 2.5.6 3.6.1.3 0 .7-.2 1z"/></svg>(+00) 000 000</div>
    <div class="row"><svg width="14" height="16" viewBox="0 0 14 18"><path d="M7 1a5.5 5.5 0 0 0-5.5 5.5C1.5 11 7 17 7 17s5.5-6 5.5-10.5A5.5 5.5 0 0 0 7 1z" fill="none" stroke="#fff" stroke-width="1.6"/><circle cx="7" cy="6.5" r="2" fill="#fff"/></svg>Lorem Ipsum Dolor Sit Amet, 70000</div>
    <div class="row"><svg width="14" height="11" viewBox="0 0 26 20"><rect x="1" y="1" width="24" height="18" fill="none" stroke="#fff" stroke-width="2.5"/><path d="M1 1l12 10L25 1" fill="none" stroke="#fff" stroke-width="2.5"/></svg>info@rivolex.com</div>
  </div>
  <div class="group" style="top:340px">
    <b>Customer Services</b>
    <div class="row"><svg width="14" height="14" viewBox="0 0 24 24"><path fill="#fff" d="M6.6 10.8a15 15 0 0 0 6.6 6.6l2.2-2.2c.3-.3.7-.4 1-.2 1.1.4 2.3.6 3.6.6.6 0 1 .4 1 1V20c0 .6-.4 1-1 1A17 17 0 0 1 3 4c0-.6.4-1 1-1h3.5c.6 0 1 .4 1 1 0 1.3.2 2.5.6 3.6.1.3 0 .7-.2 1z"/></svg>(+00) 000 000</div>
    <div class="row"><svg width="14" height="11" viewBox="0 0 26 20"><rect x="1" y="1" width="24" height="18" fill="none" stroke="#fff" stroke-width="2.5"/><path d="M1 1l12 10L25 1" fill="none" stroke="#fff" stroke-width="2.5"/></svg>cs@rivolex.com</div>
  </div>
  <span class="pill" style="left:74px">VISIT OUR BLOG</span>
  <span class="pill" style="left:201px">NEW TECHNOLOGY</span>
</section>
<div class="abs map" role="img" aria-label="Street map of the company's city area"></div>

<footer class="abs footer">Copyright 2017, rivolex. All Rights Reserved</footer>

</body>
</html>
```